Sleep Consulting Business

Hello I need a business card design with similar colors to my logo that was created. I help mom/parents whose little ones are having sleep issues. Are you able to recreate the picture with the girl sleeping onto a business card using a picture that I provide. That would be one side with my logo on top and on the other side would the following:
My name (in bigger letters than the rest. maybe written in script
title
email
website
phone
instagram
I have included color Inspo
Full Name, number, email, website, ig page

```html
<!DOCTYPE html>
<html lang="en">
<head>
<meta charset="utf-8">
<title>Bramblewood Sleep Co. – Business Card</title>
<link href="https://fonts.googleapis.com/css2?family=Poppins:wght@400&family=Allura&display=swap" rel="stylesheet">
<style>
  :root {
    --stage: #2e2e2e;
    --card-dark: #1f1a17;
    --card-dark-2: #3a2e26;
    --tan: #c3a68b;
    --cream: #efe4da;
    --white: #ffffff;
  }
  html, body {
    margin: 0;
    width: 1200px;
    height: 689px;
    overflow: hidden;
    background: var(--stage);
  }
  .canvas {
    position: relative;
    width: 1200px;
    height: 689px;
    display: flex;
    align-items: center;
    justify-content: center;
    gap: 48px;
  }
  .card {
    position: relative;
    width: 520px;
    height: 298px;
    border-radius: 18px;
    overflow: hidden;
    box-shadow: 0 18px 40px rgba(0,0,0,0.45);
  }
  /* Front */
  .card-front { background: var(--card-dark); }
  .card-front .photo {
    position: absolute;
    inset: 0;
    background:
      radial-gradient(ellipse at 62% 30%, rgba(120,92,72,0.55), transparent 60%),
      linear-gradient(160deg, var(--card-dark-2), var(--card-dark) 70%);
  }
  .brand {
    position: absolute;
    inset: 0;
    display: flex;
    align-items: center;
    justify-content: center;
  }
  .brand-name {
    font-family: "Poppins", sans-serif;
    font-weight: 400;
    font-size: 34px;
    letter-spacing: 1px;
    color: var(--cream);
  }
  /* Back */
  .card-back {
    background: var(--tan);
    color: var(--white);
  }
  .identity {
    position: absolute;
    top: 52px;
    left: 0;
    right: 0;
    text-align: center;
  }
  .person-name {
    font-family: "Allura", cursive;
    font-size: 62px;
    line-height: 1;
    margin: 0;
    font-weight: 400;
  }
  .person-title {
    font-family: "Poppins", sans-serif;
    font-size: 12px;
    letter-spacing: 1.5px;
    margin: 6px 0 0;
    text-transform: uppercase;
  }
  .identity-rule {
    width: 90px;
    height: 1px;
    background: rgba(255,255,255,0.75);
    margin: 12px auto 0;
  }
  .contacts {
    position: absolute;
    left: 0;
    right: 0;
    bottom: 52px;
    display: flex;
    justify-content: center;
    align-items: center;
    gap: 20px;
    font-family: "Poppins", sans-serif;
    font-size: 12px;
    letter-spacing: 0.5px;
  }
  .contact-col { display: flex; flex-direction: column; gap: 8px; }
  .contact-col--left { align-items: flex-end; text-align: right; }
  .contact-col--right { align-items: flex-start; }
  .contact-divider {
    width: 1px;
    height: 48px;
    background: rgba(255,255,255,0.75);
  }
  .contact-item { display: flex; align-items: center; gap: 7px; white-space: nowrap; }
  .icon { width: 13px; height: 13px; flex: none; }
</style>
</head>
<body>
<main class="canvas">
  <section class="card card-front">
    <div class="photo" role="img" aria-label="Dimly lit photograph of a child sleeping under warm brown bedding"></div>
    <div class="brand">
      <span class="brand-name">Bramblewood Sleep Co.</span>
    </div>
  </section>

  <section class="card card-back">
    <div class="identity">
      <h1 class="person-name">Elliot Marsh</h1>
      <p class="person-title">Managing Director</p>
      <div class="identity-rule"></div>
    </div>
    <div class="contacts">
      <div class="contact-col contact-col--left">
        <div class="contact-item">055-210 384 617
          <svg class="icon" viewBox="0 0 24 24" fill="none" stroke="currentColor" stroke-width="2"><path d="M5 3h4l2 5-3 2a12 12 0 0 0 6 6l2-3 5 2v4a2 2 0 0 1-2 2A18 18 0 0 1 3 5a2 2 0 0 1 2-2z"/></svg>
        </div>
        <div class="contact-item">HELLO@BRAMBLEWOOD.COM
          <svg class="icon" viewBox="0 0 24 24" fill="none" stroke="currentColor" stroke-width="2"><rect x="2" y="5" width="20" height="14" rx="1"/><path d="M2 6l10 7 10-7"/></svg>
        </div>
      </div>
      <div class="contact-divider"></div>
      <div class="contact-col contact-col--right">
        <div class="contact-item">
          <svg class="icon" viewBox="0 0 24 24" fill="none" stroke="currentColor" stroke-width="2"><circle cx="12" cy="12" r="10"/><path d="M2 12h20M12 2c3 3 3 17 0 20M12 2c-3 3-3 17 0 20"/></svg>
          WWW.BRAMBLEWOOD.COM
        </div>
        <div class="contact-item">
          <svg class="icon" viewBox="0 0 24 24" fill="none" stroke="currentColor" stroke-width="2"><circle cx="12" cy="12" r="9"/></svg>
          INSTAGRAM.BRAMBLEWOOD
        </div>
      </div>
    </div>
  </section>
</main>
</body>
</html>
```